Fitness Equipment Repair Business Needs a Catchy New Business Card

We have an existing business card, however, it is quite plain and boring. We are expanding primarily in the commercial area (gyms, studios, apartment complexes etc). The business card will serve as eye candy to those managers/owners that can't be met for a face to face.
Originally I was planning for a brochure as well, but all of our information is better summarized on our website. (brasswheelservicing.ca).
I would like the card to match the colour scheme of the website and utilize the logo. It should have a professional clean feel to it, however, a little colouring outside the lines wouldn't hurt.
The example card is for my service technician (Corwin Haldane). If possible I would like to be able to edit the text to use for more than one person.

Industry/Entity Type

Appliance Repair

Contact Information for Business Card

Clean, crisp and professional but needs to be eye catching. Preferably using the black, white and red colour scheme matching the website. Double sided would be nice, but is not necessary.

Colors
ec1f27
ffffff
000000

Requirements
Must have
• Must be able to edit name, phone number and title to use for multiple people. Must show the company website (brasswheelservicing.ca).

```html
<!DOCTYPE html>
<html lang="en">
<head>
<meta charset="utf-8">
<title>Brass Wheel Servicing – Business Card</title>
<link rel="stylesheet" href="https://fonts.googleapis.com/css2?family=Jost:wght@400;500&display=swap">
<style>
  :root {
    --page-bg: #e4e2df;
    --card-black: #050505;
    --card-lift: #2e2e2e;
    --brand-red: #ec1f27;
    --text-white: #ffffff;
    --text-silver: #d6d6d6;
    --text-muted: #bdbdbd;
    --art-light: #5a5a5a;
    --art-dark: #141414;
  }
  * { margin: 0; padding: 0; box-sizing: border-box; }
  html, body {
    width: 1200px; height: 969px; overflow: hidden;
    background: var(--page-bg);
    font-family: "Jost", "Futura", sans-serif;
  }
  .canvas { position: relative; width: 1200px; height: 969px; }
  .business-card {
    position: absolute; left: 100px; top: 200px;
    width: 1000px; height: 568px;
    background: radial-gradient(ellipse at 18% 20%, var(--card-lift) 0%, #141414 40%, var(--card-black) 75%);
    border-radius: 6px;
    box-shadow: 0 18px 40px rgba(0,0,0,0.28);
    overflow: hidden;
  }
  .mascot-art {
    position: absolute; left: 52px; top: 44px;
    width: 352px; height: 440px;
    border-radius: 40% 40% 8px 8px;
    background: linear-gradient(160deg, var(--art-light) 0%, #2a2a2a 55%, var(--art-dark) 100%);
    opacity: 0.85;
  }
  .brand-name {
    position: absolute; left: 56px; top: 500px;
    font-size: 30px; font-weight: 500; letter-spacing: 2px;
    color: var(--text-silver); line-height: 1;
  }
  .details {
    position: absolute; right: 48px; top: 88px;
    text-align: right;
  }
  .company-name {
    font-size: 34px; font-weight: 500; letter-spacing: 3px;
    font-variant: small-caps; color: var(--text-silver);
    margin-bottom: 44px;
  }
  .person-name {
    font-size: 36px; font-weight: 500; font-variant: small-caps;
    letter-spacing: 1.5px; color: var(--brand-red); line-height: 1.1;
  }
  .person-role {
    font-size: 27px; font-variant: small-caps; letter-spacing: 1.5px;
    color: var(--text-muted); margin-bottom: 22px;
  }
  .address { font-size: 25px; color: var(--text-white); line-height: 1.2; margin-bottom: 20px; }
  .contact-list { list-style: none; }
  .contact-list li {
    display: flex; justify-content: flex-end; align-items: center; gap: 14px;
    font-size: 24px; color: var(--text-muted); line-height: 1.65;
  }
  .contact-list svg { width: 20px; height: 20px; fill: var(--brand-red); flex: none; }
</style>
</head>
<body>
<div class="canvas">
  <section class="business-card">
    <div class="mascot-art" role="img" aria-label="Line illustration of a muscular technician holding a wrench"></div>
    <div class="brand-name">Brass Wheel</div>

    <div class="details">
      <h1 class="company-name">Brass Wheel Servicing</h1>
      <p class="person-name">Corwin Haldane</p>
      <p class="person-role">Service technician</p>
      <p class="address">1785 Corrie Lane NW<br>Edmonton AB T5X 2K9</p>
      <ul class="contact-list">
        <li>587-555-0142
          <svg viewBox="0 0 24 24"><path d="M6.6 10.8a15 15 0 0 0 6.6 6.6l2.2-2.2a1 1 0 0 1 1-.25 11.4 11.4 0 0 0 3.6.6 1 1 0 0 1 1 1V20a1 1 0 0 1-1 1A17 17 0 0 1 3 4a1 1 0 0 1 1-1h3.5a1 1 0 0 1 1 1c0 1.25.2 2.45.6 3.6a1 1 0 0 1-.25 1z"/></svg></li>
        <li>780-555-0187
          <svg viewBox="0 0 24 24"><path d="M6.6 10.8a15 15 0 0 0 6.6 6.6l2.2-2.2a1 1 0 0 1 1-.25 11.4 11.4 0 0 0 3.6.6 1 1 0 0 1 1 1V20a1 1 0 0 1-1 1A17 17 0 0 1 3 4a1 1 0 0 1 1-1h3.5a1 1 0 0 1 1 1c0 1.25.2 2.45.6 3.6a1 1 0 0 1-.25 1z"/></svg></li>
        <li>brasswheel@inbox.ca
          <svg viewBox="0 0 24 24"><path d="M2 5h20v2l-10 7L2 7z"/><path d="M2 9l10 7 10-7v10H2z"/></svg></li>
        <li>www.brasswheelservicing.ca
          <svg viewBox="0 0 24 24"><circle cx="12" cy="12" r="10"/><path d="M2 12h20M12 2c3 3 3 17 0 20M12 2c-3 3-3 17 0 20" fill="none" stroke="#050505" stroke-width="1.6"/></svg></li>
      </ul>
    </div>
  </section>
</div>
</body>
</html>
```